KorvaniteX a Canadian Brand

I'm looking for a new name card design together with our new brand "KorvaniteX"! FYI, KorvaniteX is a new developed compounds for raw plastic material in order to improve the Physical properties。

Target Market(s)

Worldwide

Industry/Entity Type

Plastic

```html
<!DOCTYPE html>
<html lang="en">
<head>
<meta charset="utf-8">
<title>KorvaniteX Business Card</title>
<link href="https://fonts.googleapis.com/css2?family=Montserrat:wght@400;500;700;800&display=swap" rel="stylesheet">
<style>
  :root {
    --brand-green: #066a3a;
    --brand-grey: #5c5c5c;
    --text-grey: #4a4a4a;
    --card-white: #ffffff;
    --backdrop: #cfcfcf;
    --shadow: rgba(0, 0, 0, 0.45);
  }
  * { margin: 0; padding: 0; box-sizing: border-box; }
  html, body { width: 1200px; height: 1000px; overflow: hidden; }
  body {
    background: var(--backdrop);
    font-family: "Montserrat", Arial, sans-serif;
    position: relative;
  }
  .card {
    position: absolute;
    top: 52px;
    width: 534px;
    height: 313px;
    background: var(--card-white);
    box-shadow: 6px 8px 10px var(--shadow);
    overflow: hidden;
  }
  .card--front { left: 53px; }
  .card--back { left: 628px; }
  .block { position: absolute; }
  .block--green { background: var(--brand-green); }
  .block--grey { background: var(--brand-grey); }

  .wordmark {
    position: absolute;
    font-weight: 800;
    color: var(--brand-green);
    letter-spacing: -0.5px;
    line-height: 1;
  }
  .card--front .wordmark { left: 30px; top: 38px; font-size: 42px; }
  .card--back .wordmark { left: 0; width: 100%; text-align: center; top: 127px; font-size: 44px; }

  .name-band { left: 0; top: 114px; width: 332px; height: 77px; }
  .name-band .person-name {
    position: absolute; left: 42px; top: 17px;
    color: #fff; font-size: 25px; font-weight: 500; letter-spacing: 0.3px;
  }
  .name-band .person-title {
    position: absolute; left: 42px; top: 48px;
    color: #fff; font-size: 15px; font-weight: 500;
  }

  .contact-list {
    position: absolute; top: 234px;
    list-style: none;
  }
  .contact-list--phones { left: 42px; }
  .contact-list--web { left: 259px; }
  .contact-list li {
    display: flex; align-items: center; gap: 8px;
    height: 20px;
    font-size: 15px; color: var(--text-grey);
  }
  .contact-icon { width: 16px; height: 16px; flex: none; }

  .domain {
    position: absolute; left: 0; width: 100%; text-align: center;
    top: 177px; font-size: 15px; font-weight: 500; color: var(--text-grey);
  }
</style>
</head>
<body>

  <section class="card card--front" aria-label="Card front">
    <div class="wordmark">KorvaniteX</div>
    <div class="block block--green name-band">
      <span class="person-name">YOUR NAME</span>
      <span class="person-title">TITLE</span>
    </div>
    <div class="block block--grey" style="left:347px; top:114px; width:115px; height:77px;"></div>
    <div class="block block--green" style="left:475px; top:114px; width:59px; height:77px;"></div>

    <ul class="contact-list contact-list--phones">
      <li>
        <svg class="contact-icon" viewBox="0 0 16 16" aria-hidden="true">
          <circle cx="8" cy="8" r="8" fill="var(--brand-green)"/>
          <path d="M5 4.5l2 2-1 1c.6 1.2 1.3 1.9 2.5 2.5l1-1 2 2-1.3 1.3C7 12 4 9 3.7 5.8z" fill="#fff"/>
        </svg>
        123-456-7890
      </li>
      <li>
        <svg class="contact-icon" viewBox="0 0 16 16" aria-hidden="true">
          <circle cx="8" cy="8" r="8" fill="var(--brand-green)"/>
          <rect x="5.5" y="3.5" width="5" height="9" rx="1" fill="#fff"/>
          <rect x="6.5" y="5" width="3" height="5" fill="var(--brand-green)"/>
        </svg>
        123-546-7890
      </li>
    </ul>

    <ul class="contact-list contact-list--web">
      <li>
        <svg class="contact-icon" viewBox="0 0 16 16" aria-hidden="true">
          <circle cx="8" cy="8" r="8" fill="var(--brand-green)"/>
          <rect x="4" y="5" width="8" height="6" fill="#fff"/>
          <path d="M4 5l4 3.5L12 5" fill="none" stroke="var(--brand-green)" stroke-width="1"/>
        </svg>
        name@yourdomain.com
      </li>
      <li>
        <svg class="contact-icon" viewBox="0 0 16 16" aria-hidden="true">
          <circle cx="8" cy="8" r="8" fill="var(--brand-green)"/>
          <circle cx="8" cy="8" r="4" fill="none" stroke="#fff" stroke-width="1.2"/>
          <path d="M4 8h8M8 4v8" stroke="#fff" stroke-width="1"/>
        </svg>
        www.yourdomain.com
      </li>
    </ul>
  </section>

  <section class="card card--back" aria-label="Card back">
    <div class="block block--green" style="left:0; top:0; width:332px; height:31px;"></div>
    <div class="block block--grey" style="left:347px; top:0; width:115px; height:31px;"></div>
    <div class="block block--green" style="left:476px; top:0; width:58px; height:31px;"></div>

    <div class="wordmark">KorvaniteX</div>
    <div class="domain">www.yourdomain.com</div>

    <div class="block block--green" style="left:0; top:283px; width:58px; height:30px;"></div>
    <div class="block block--grey" style="left:72px; top:283px; width:115px; height:30px;"></div>
    <div class="block block--green" style="left:202px; top:283px; width:332px; height:30px;"></div>
  </section>

</body>
</html>
```